2 x storefront vinyl request

We are transitioning to a storefront office and need two vinyls for the windows.

First vinyl: Use the Aldwick Partners logo, website (www.aldwickpartnersestates.example) and leasing office number ((555) 318-4726)

Second vinyl: Maintenance Division & phone number (555) 318-4726

```html
<!DOCTYPE html>
<html lang="en">
<head>
<meta charset="utf-8">
<title>Aldwick Partners – Storefront Vinyls</title>
<link rel="stylesheet" href="https://fonts.googleapis.com/css2?family=Roboto:wght@500;700&display=swap">
<style>
  :root {
    --backdrop: #8e8e90;
    --vinyl-white: #ffffff;
    --ink: #000000;
    --reverse-text: #ffffff;
  }
  * { box-sizing: border-box; margin: 0; padding: 0; }
  html, body { width: 1200px; height: 1000px; overflow: hidden; }
  body {
    position: relative;
    background: var(--backdrop);
    font-family: "Roboto", Arial, sans-serif;
  }
  .vinyl {
    position: absolute;
    left: 253px;
    width: 695px;
    background: var(--vinyl-white);
  }
  .vinyl--leasing { top: 18px; height: 469px; }
  .vinyl--maintenance { top: 514px; height: 468px; }
  .vinyl__frame {
    position: absolute;
    left: 22px; right: 22px; top: 25px; bottom: 24px;
    border: 11px solid var(--ink);
  }
  .brand-lockup {
    position: absolute;
    left: 0; right: 0; top: 60px; height: 196px;
    display: flex;
    align-items: center;
    justify-content: center;
    gap: 22px;
  }
  .brand-lockup__square {
    width: 110px; height: 110px;
    background: var(--ink);
    flex: none;
  }
  .brand-name {
    color: var(--ink);
    font-weight: 700;
    font-size: 26px;
    line-height: 1.2;
    letter-spacing: 0.3px;
  }
  .info-panel {
    position: absolute;
    background: var(--ink);
    border-radius: 8px;
    color: var(--reverse-text);
    text-align: center;
    font-weight: 500;
  }
  .vinyl--leasing .info-panel { left: 46px; width: 603px; top: 284px; height: 130px; }
  .info-panel__web { font-size: 26px; font-weight: 700; margin-top: 8px; line-height: 30px; }
  .info-panel__label { font-size: 25px; font-weight: 700; margin-top: 20px; line-height: 30px; }
  .info-panel__phone { font-size: 25px; font-weight: 700; line-height: 32px; }
  .vinyl--maintenance .info-panel { left: 56px; width: 584px; top: 260px; height: 147px; }
  .info-panel__title { font-size: 48px; font-weight: 700; line-height: 56px; margin-top: 16px; }
  .info-panel__phone--large { font-size: 48px; font-weight: 500; line-height: 58px; }
  .division-mark {
    position: absolute;
    left: 227px; top: 59px;
    width: 242px; height: 177px;
  }
</style>
</head>
<body>
  <section class="vinyl vinyl--leasing">
    <div class="vinyl__frame"></div>
    <div class="brand-lockup">
      <div class="brand-lockup__square"></div>
      <div class="brand-name">ALDWICK<br>PARTNERS<br>PROPERTIES</div>
    </div>
    <div class="info-panel">
      <p class="info-panel__web">WWW.ALDWICKPARTNERSESTATES.EXAMPLE</p>
      <p class="info-panel__label">LEASING OFFICE NUMBER</p>
      <p class="info-panel__phone">(555) 318-4726</p>
    </div>
  </section>

  <section class="vinyl vinyl--maintenance">
    <div class="vinyl__frame"></div>
    <svg class="division-mark" viewBox="0 0 242 177" role="img" aria-label="Maintenance division emblem">
      <rect x="0" y="0" width="242" height="177" fill="#000000"/>
    </svg>
    <div class="info-panel">
      <p class="info-panel__title">MAINTENANCE DIVISION</p>
      <p class="info-panel__phone--large">(555) 318-4726)</p>
    </div>
  </section>
</body>
</html>
```